Velmora Brightstead Website

Create website for Legal Management Company which specializes in Law Office Spersriinal Management
System implementation & Training
Global presence
Paralegal Services - Remote or In-Office
Legal Research
- Judge Motion Ruling History
- Opposing Counsel Opposition Research - Historical Filings - Pattern identification
Service by Mail - Ex- Parte Notice

Probate -Heir Finder - Asset Location -

```html
<!DOCTYPE html>
<html lang="en">
<head>
<meta charset="utf-8">
<title>Velmora Brightstead – Legal Management &amp; Paralegal Services</title>
<link href="https://fonts.googleapis.com/css2?family=Montserrat:wght@400;500;600;700;800&display=swap" rel="stylesheet">
<style>
:root{
  --navy:#0b1a45;
  --navy-deep:#040d2e;
  --orange:#f5a431;
  --ink:#0d1733;
  --text:#3a3f4d;
  --muted:#5a5f6b;
  --light:#f7f7f7;
  --white:#ffffff;
  --contact-bg:#e4eaf7;
}
*{box-sizing:border-box;margin:0;padding:0}
html,body{width:725px;height:1200px;overflow:hidden;background:var(--white)}
body{font-family:'Montserrat',sans-serif;color:var(--text)}
.page{width:725px;height:1200px;position:relative;overflow:hidden}

/* hero */
.hero{position:relative;height:398px;background:var(--light)}
.hero-art{position:absolute;inset:0;border-radius:0 0 50% 50% / 0 0 120px 120px;
  background:
    radial-gradient(ellipse 40% 45% at 22% 55%, rgba(245,164,49,.55), rgba(245,164,49,0) 70%),
    radial-gradient(ellipse 60% 55% at 62% 45%, #1d4f9f 0%, #0f2d6e 45%, var(--navy-deep) 85%);
  overflow:hidden}
.hero-art::after{content:"";position:absolute;left:0;right:0;bottom:0;height:60px;
  background:linear-gradient(180deg,rgba(245,164,49,0),rgba(245,164,49,.35))}
.nav{position:absolute;top:0;left:0;right:0;height:50px;display:flex;align-items:center;justify-content:space-between;padding:0 14px 0 11px;z-index:2}
.brand{display:flex;align-items:center;gap:6px;color:var(--orange);font-weight:600;font-size:12px;letter-spacing:.3px;line-height:1.05;text-transform:uppercase}
.brand-mark{width:14px;height:14px;border:1.5px solid var(--orange);border-radius:2px}
.menu{display:flex;align-items:center;gap:18px;list-style:none;font-size:8.5px;font-weight:500;color:var(--white)}
.menu .active{color:var(--orange);font-weight:700;position:relative}
.menu .active::after{content:"";position:absolute;left:35%;right:35%;bottom:-4px;height:1px;background:var(--orange)}
.menu .cta{background:var(--orange);color:var(--navy);padding:4px 6px}
.hero-copy{position:absolute;left:291px;width:350px;top:125px;text-align:center;color:var(--white);z-index:2}
.hero-copy h1{font-size:20px;font-weight:700;line-height:1.25;letter-spacing:.2px;text-transform:uppercase}
.hero-copy p{font-size:8.3px;line-height:1.75;margin-top:8px}
.btn-outline{display:inline-block;margin-top:9px;border:1px solid var(--orange);color:var(--orange);font-weight:700;font-size:8.5px;padding:5px 7px;letter-spacing:.2px}
.hero-badge{position:absolute;left:342px;top:381px;width:40px;height:38px;background:var(--white);border:2px solid var(--orange);border-radius:5px;z-index:3}

/* services */
.services{background:var(--light);height:242px;padding-top:37px;text-align:center}
.section-title{font-size:19px;font-weight:800;color:var(--navy);letter-spacing:.3px;text-transform:uppercase;line-height:23px}
.cards{display:flex;gap:12px;justify-content:center;margin-top:12px}
.card{width:109px;height:130px;background:var(--white);border-radius:3px;box-shadow:0 1px 4px rgba(0,0,0,.06);padding:14px 8px 0}
.card svg{width:14px;height:14px}
.card h3{font-size:7px;font-weight:700;color:var(--ink);line-height:1.45;margin-top:8px}
.card p{font-size:5.2px;line-height:1.65;color:var(--muted);margin-top:5px}

/* about */
.about{height:336px;background:var(--white);display:flex;padding:41px 0 0 66px;gap:26px}
.about-media{width:283px;display:flex;flex-direction:column;gap:6px}
.photo.team{height:122px;border-radius:8px 8px 0 0;background:linear-gradient(135deg,#b9593f,#8e3b2b 60%,#3a2a30)}
.photo.office{height:122px;border-radius:0 0 8px 8px;background:linear-gradient(180deg,#c4644a,#a44832 70%,#4a2a22)}
.about-copy{width:250px;padding-top:34px}
.about-copy h2{font-size:20px;font-weight:800;color:var(--navy);text-transform:uppercase;line-height:22px}
.about-copy p{font-size:6.4px;line-height:9.6px;color:var(--text);margin-top:9px}
.about-copy h2 + p{margin-top:2px}
.btn-solid{display:inline-block;background:var(--orange);color:var(--navy);font-weight:700;font-size:6.8px;padding:4px 7px;margin-top:12px}

/* contact */
.contact{height:188px;background:var(--contact-bg);position:relative;display:flex;align-items:flex-start;padding:40px 0 0 66px}
.contact-intro{width:170px}
.contact-intro h2{font-size:19px;font-weight:800;color:var(--navy);text-transform:uppercase;line-height:22px}
.contact-intro p{font-size:7px;line-height:1.45;color:var(--text);margin-top:3px}
.form{width:183px;margin-left:7px;display:flex;flex-direction:column;gap:3px;position:relative;z-index:1}
.form .row{display:flex;gap:3px}
.field{display:block;background:var(--white);font-size:6px;color:var(--muted);padding:5px 6px;height:17px;line-height:7px}
.row .field{flex:1}
.field.message{height:39px}
.btn-send{align-self:flex-end;background:var(--orange);color:var(--navy);font-weight:700;font-size:6.8px;padding:4px 7px;margin-top:1px}
.contact-art{position:absolute;right:0;top:0;width:252px;height:188px;
  background:radial-gradient(ellipse 60% 55% at 55% 50%,#c6d2ee,#dde5f6 55%,rgba(228,234,247,0) 80%)}

/* footer */
.footer{height:36px;background:var(--navy-deep);color:var(--white);text-align:center;padding-top:8px}
.footer ul{list-style:none;display:flex;justify-content:center;gap:23px;font-size:6.5px}
.footer small{display:block;font-size:6.2px;margin-top:5px}
</style>
</head>
<body>
<div class="page">

  <header class="hero">
    <div class="hero-art" role="img" aria-label="Golden scales of justice glowing in front of a blue world map"></div>
    <nav class="nav">
      <div class="brand"><span class="brand-mark"></span><span>Velmora<br>Brightstead</span></div>
      <ul class="menu">
        <li class="active">HOME</li>
        <li>SERVICES</li>
        <li>ABOUT</li>
        <li>BLOG</li>
        <li>TEAM</li>
        <li class="cta">CONTACT</li>
      </ul>
    </nav>
    <div class="hero-copy">
      <h1>Comprehensive Legal Management &amp; Paralegal Services</h1>
      <p>Implementing law office systems, providing expert paralegal support<br>and performing in-depth legal research worldwide.</p>
      <span class="btn-outline">SCHEDULE A CONSULTATION</span>
    </div>
    <div class="hero-badge"></div>
  </header>

  <section class="services">
    <h2 class="section-title">Our Services</h2>
    <div class="cards">
      <article class="card">
        <svg viewBox="0 0 16 16"><circle cx="8" cy="8" r="5" fill="none" stroke="#6b7280" stroke-width="2.4" stroke-dasharray="2 1.4"/><circle cx="8" cy="8" r="2.2" fill="#6b7280"/></svg>
        <h3>Management System Implementation &amp; Training</h3>
        <p>Deploy custom law office management systems and train your team to streamline operations and ensure compliance.</p>
      </article>
      <article class="card">
        <svg viewBox="0 0 16 16"><circle cx="5.5" cy="5.5" r="2.5" fill="#4a6fa5"/><circle cx="10.5" cy="5.5" r="2.5" fill="#4a6fa5"/><path d="M1 14c0-3 2-5 4.5-5S10 11 10 14zM6 14c0-3 2-5 4.5-5S15 11 15 14z" fill="#4a6fa5"/></svg>
        <h3>Paralegal Services</h3>
        <p>Certified paralegals available remotely or on-site to assist with document preparation, filings and case management.</p>
      </article>
      <article class="card">
        <svg viewBox="0 0 16 16"><circle cx="6.5" cy="6.5" r="4" fill="#eef3f8" stroke="#555" stroke-width="1.4"/><path d="M9.5 9.5l4.5 4.5" stroke="#333" stroke-width="2" stroke-linecap="round"/></svg>
        <h3>Legal Research</h3>
        <p>Comprehensive research including motion ruling history, opposing counsel research and pattern identification of historical filings.</p>
      </article>
      <article class="card">
        <svg viewBox="0 0 16 16"><rect x="1.5" y="4" width="13" height="8.5" fill="#e5e7eb" stroke="#b8bcc4" stroke-width=".8"/><path d="M1.5 4l6.5 5 6.5-5" fill="none" stroke="#b8bcc4" stroke-width=".8"/></svg>
        <h3>Service by Mail</h3>
        <p>Efficient handling of ex-parte notices and legal document service by mail in domestic and international jurisdictions.</p>
      </article>
      <article class="card">
        <svg viewBox="0 0 16 16"><circle cx="8" cy="5" r="3.2" fill="#d9383a"/><path d="M8 8v7" stroke="#888" stroke-width="1.2"/></svg>
        <h3>Probate &amp; Asset Location</h3>
        <p>Locate heirs and identify assets to simplify probate proceedings and ensure equitable distribution.</p>
      </article>
    </div>
  </section>

  <section class="about">
    <div class="about-media">
      <div class="photo team" role="img" aria-label="Team of four legal professionals in business attire"></div>
      <div class="photo office" role="img" aria-label="Staff standing in a terracotta-walled office with company lettering"></div>
    </div>
    <div class="about-copy">
      <h2>About Us</h2>
      <p>Velmora Brightstead is a global legal management company dedicated to empowering law firms with modern systems, expert paralegal support and thorough legal research.</p>
      <p>Our team brings decades of experience in law office operations, technology and procedural compliance. We are committed to professionalism, efficiency and accuracy—helping firms increase productivity and deliver superior outcomes for their clients.</p>
      <p>Lorem ipsum dolor sit amet, consectetuer adipiscing elit, sed diam nonummy nibh euismod tincidunt ut laoreet dolore magna aliquam erat volutpat. Ut wisi enim ad minim veniam, quis nostrud exerci tation ullamcorper suscipit lobortis nisl ut aliquip ex ea commodo consequat. Duis autem vel eum iriure dolor.</p>
      <span class="btn-solid">LEARN MORE</span>
    </div>
  </section>

  <section class="contact">
    <div class="contact-intro">
      <h2>Contact Us</h2>
      <p>Ready to transform your legal operations? Reach out for a free consultation.</p>
    </div>
    <div class="form">
      <div class="row"><span class="field">Your name</span><span class="field">Your phone number</span></div>
      <span class="field">Your email</span>
      <span class="field message">Your message...</span>
      <span class="btn-send">SEND MESSAGE</span>
    </div>
    <div class="contact-art" role="img" aria-label="Isometric laptop with analytics charts on a desk with office supplies"></div>
  </section>

  <footer class="footer">
    <ul><li>HOME</li><li>SERVICES</li><li>ABOUT</li><li>BLOG</li><li>TEAM</li><li>CONTACT</li></ul>
    <small>© 2025 Velmora Brightstead. All rights reserved.</small>
  </footer>

</div>
</body>
</html>
```